Psychology and Counselling Relationship Centre wants a Website

We need a SEO Website that is professional and simple Company Logo and colours is done and supplied

Target Market(s)

People wanting marriage Counselling / Parenting Issues / Relationship issues

Industry/Entity Type

Psychology

Coding

Coded - Design and coding required

Number of Pages Required

5+ page

Font styles to use
Other font styles liked:
• calibri

Colors
32a6d6
33b8a4
0758a5

Requirements
Must have
• Simple easy layout
• Page by page link
• Easy to navigate
• Professional and Welcoming

```html
<!DOCTYPE html>
<html lang="en">
<head>
<meta charset="utf-8">
<title>Whole Heart Living – Psychology &amp; Counselling Relationship Centre</title>
<link rel="stylesheet" href="https://fonts.googleapis.com/css2?family=Fira+Sans:wght@400;500;600;700&family=Oswald:wght@400;500&family=Courgette&family=Poppins:wght@300;400;500&display=swap">
<style>
:root{
  --blue:#2e73b8;
  --green:#a8cb37;
  --teal:#34b3a0;
  --text:#555b63;
  --pale:#f2f5f9;
  --white:#ffffff;
}
*{box-sizing:border-box;margin:0;padding:0}
html,body{width:1200px;height:3854px;overflow:hidden}
body{font-family:"Poppins",sans-serif;color:var(--text);background:var(--white);position:relative}
section,header,footer,.topbar{position:relative;width:1200px;overflow:hidden}
.abs{position:absolute}
.btn{position:absolute;display:flex;align-items:center;justify-content:center;background:var(--green);color:var(--white);font-family:"Fira Sans",sans-serif;font-size:19px;letter-spacing:.3px;border-radius:3px;text-transform:uppercase}
.h2{font-family:"Fira Sans",sans-serif;font-weight:600;font-size:37px;color:var(--blue);text-transform:uppercase}
.h2 span{color:var(--green)}
.photo{position:absolute}

/* top bar */
.topbar{height:42px;background:var(--blue);color:var(--white);font-size:14px}
.topbar .call{position:absolute;left:681px;top:12px}
.topbar .num{position:absolute;top:6px;display:flex;align-items:center;gap:8px;font-weight:500;font-size:15px}
.topbar .num i{width:29px;height:29px;border-radius:50%;background:var(--green);display:flex;align-items:center;justify-content:center}
.topbar .sep{position:absolute;left:962px;top:10px}

/* header */
.site-header{height:82px;background:var(--white)}
.brand-mark{position:absolute;left:77px;top:22px;width:36px;height:36px;border-radius:50%;background:var(--green)}
.brand-name{position:absolute;left:123px;top:22px;font-family:"Fira Sans",sans-serif;font-weight:600;font-size:19px;color:var(--blue);line-height:1.1}
.brand-sub{position:absolute;left:123px;top:46px;font-size:8.5px;font-weight:500;color:var(--blue);letter-spacing:.1px}
.nav{position:absolute;left:312px;top:30px;display:flex;gap:22px;font-size:15px;color:#333;align-items:center}

/* hero */
.hero{height:552px;background:linear-gradient(90deg,#f4f4f4 0%,#eeeeee 45%,#e6e6e6 100%)}
.hero .photo{left:440px;top:0;width:760px;height:552px;background:linear-gradient(100deg,#eceae6 0%,#d9dcd6 45%,#c9d4d9 70%,#e1e4e3 100%)}
.hero h1{position:absolute;left:77px;top:150px;font-family:"Oswald",sans-serif;font-weight:400;font-size:43px;line-height:47px;color:#1d1d1d}
.hero .tag{position:absolute;left:77px;top:308px;font-family:"Courgette",cursive;font-size:19px;color:var(--blue)}
.hero .arrow{position:absolute;top:257px;width:46px;height:46px;border-radius:50%;background:var(--white);display:flex;align-items:center;justify-content:center}

/* who we help */
.who{height:510px}
.who .frame{position:absolute;left:166px;top:64px;width:289px;height:382px;background:var(--green)}
.who .photo{left:175px;top:74px;width:396px;height:364px;background:linear-gradient(120deg,#c9d0d6 0%,#9fb0c0 45%,#e8dccd 80%,#d6c9b6 100%)}
.who .h2{position:absolute;left:631px;top:106px}
.who p{position:absolute;left:637px;top:162px;width:400px;font-size:13.5px;line-height:27px}

/* what to expect */
.expect{height:693px;background:var(--pale);text-align:center}
.expect .h2{position:absolute;left:0;width:1200px;top:62px}
.expect .lead{position:absolute;left:295px;top:117px;width:610px;font-size:13.5px;line-height:27px}
.group{position:absolute;width:260px}
.group h3{font-family:"Fira Sans",sans-serif;font-weight:400;font-size:18px;color:var(--blue);text-transform:uppercase;line-height:22px}
.group p{font-size:14.5px;line-height:21px;margin-top:6px;color:#666}
.group.left{text-align:left}
.group.right{text-align:right}
.mini{position:absolute;width:100px;height:100px;border-radius:50%}
.feature-photo{position:absolute;left:392px;top:277px;width:416px;height:352px;border-radius:40px;background:linear-gradient(100deg,#4f86c0 0%,#8fbf6a 50%,#3bb3a1 100%)}

/* courses */
.courses{height:678px;background:var(--blue);color:var(--white)}
.courses .h2{position:absolute;left:0;width:1200px;text-align:center;top:58px;color:var(--white)}
.courses .sub{position:absolute;left:0;width:1200px;text-align:center;top:110px;font-size:16px}
.tabs{position:absolute;left:112px;top:165px;display:flex;gap:11px}
.tab{height:51px;padding:0 11px;border:1px solid rgba(255,255,255,.25);border-radius:3px;display:flex;align-items:center;font-size:14.5px;color:var(--white)}
.tab.active{background:var(--green);border-color:var(--green);font-size:19px;padding:0 14px}
.course-card{position:absolute;left:112px;top:239px;width:991px;height:374px;background:var(--white)}
.course-card .photo{left:0;top:0;width:470px;height:374px;background:linear-gradient(110deg,#8aa37a 0%,#c7cfc0 40%,#e7e4dc 70%,#9db1c7 100%)}
.course-card h3{position:absolute;left:563px;top:75px;font-family:"Fira Sans",sans-serif;font-weight:600;font-size:34px;color:#2a2a2a}
.course-card p{position:absolute;left:564px;top:128px;width:370px;font-size:14.5px;line-height:27px;color:#666}

/* keep in touch */
.touch{height:839px;text-align:center}
.touch .h2{position:absolute;left:0;width:1200px;top:63px}
.touch .lead{position:absolute;left:300px;top:116px;width:600px;font-size:15.5px;line-height:28px;color:#555}
.touch .rule{position:absolute;left:307px;top:235px;width:573px;height:1px;background:#dcdcdc}
.contact{position:absolute;width:300px;top:193px}
.contact .ring{width:86px;height:86px;margin:0 auto;border-radius:50%;border:2px dotted #c9d98f;display:flex;align-items:center;justify-content:center;background:var(--white)}
.contact .dot{width:56px;height:56px;border-radius:50%;background:var(--green);display:flex;align-items:center;justify-content:center}
.contact h4{margin-top:15px;font-weight:400;font-size:17px;color:var(--blue)}
.contact span{display:block;margin-top:4px;font-size:16px;color:#333;letter-spacing:.6px}
.touch .respond{position:absolute;left:0;width:1200px;top:392px;font-size:35px;color:var(--blue)}
.touch .respond b{color:var(--green);font-weight:500}
.touch .forward{position:absolute;left:0;width:1200px;top:440px;font-size:18px;color:var(--green)}
.touch .photo{left:172px;top:480px;width:830px;height:359px;background:linear-gradient(90deg,#e9e6e2 0%,#cfd8e6 25%,#e8d8b4 50%,#c9545a 68%,#c7cde2 85%,#efe9df 100%);border-radius:120px 120px 0 0}

/* booking band */
.booking{height:123px;background:var(--green);color:var(--white)}
.booking h3{position:absolute;left:77px;top:37px;font-family:"Fira Sans",sans-serif;font-weight:400;font-size:26px;text-transform:uppercase}
.booking p{position:absolute;left:77px;top:74px;font-size:14px;text-transform:uppercase;letter-spacing:.3px}
.booking .outline{position:absolute;left:857px;top:34px;width:266px;height:53px;border:2px solid var(--white);border-radius:3px;display:flex;align-items:center;justify-content:center;font-family:"Fira Sans",sans-serif;font-size:19px;text-transform:uppercase}

/* footer */
.site-footer{height:335px;background:var(--blue);color:var(--white)}
.foot-brand{position:absolute;left:80px;top:60px;width:232px;text-align:center}
.foot-brand .mark{width:64px;height:64px;border-radius:50%;background:var(--white);margin:0 auto 14px}
.foot-brand .name{font-family:"Fira Sans",sans-serif;font-weight:600;font-size:20px}
.foot-brand .sub{font-size:9px;font-weight:500;margin-top:2px}
.social{position:absolute;top:187px;width:40px;height:40px;border-radius:50%;background:var(--green)}
.col{position:absolute;top:34px}
.col h5{font-family:"Fira Sans",sans-serif;font-weight:600;font-size:20px;text-transform:uppercase;margin-bottom:12px}
.col h5 span{color:var(--green)}
.col li{list-style:none;font-size:13.5px;line-height:31px}
.col .note{font-size:14.5px;line-height:25px;width:290px}
.field{width:285px;height:46px;background:var(--white);border-radius:3px;margin-top:20px;color:#999;font-size:13px;display:flex;align-items:center;padding-left:16px}
.subscribe{width:166px;height:51px;background:var(--green);border-radius:3px;margin-top:8px;display:flex;align-items:center;justify-content:center;font-family:"Fira Sans",sans-serif;font-size:19px;text-transform:uppercase}
.copy{position:absolute;left:0;width:1200px;text-align:center;top:294px;font-size:14px}
</style>
</head>
<body>

<div class="topbar">
  <span class="call">Call or Text us On :</span>
  <span class="num" style="left:824px">
    <i><svg width="14" height="14" viewBox="0 0 24 24" fill="#fff"><path d="M6.6 10.8a15.1 15.1 0 0 0 6.6 6.6l2.2-2.2c.3-.3.7-.4 1-.2 1.1.4 2.3.6 3.6.6.6 0 1 .4 1 1V20c0 .6-.4 1-1 1C10.6 21 3 13.4 3 4c0-.6.4-1 1-1h3.5c.6 0 1 .4 1 1 0 1.3.2 2.5.6 3.6.1.3 0 .7-.2 1z"/></svg></i>0400 111 222
  </span>
  <span class="sep">|</span>
  <span class="num" style="left:980px">
    <i><svg width="12" height="15" viewBox="0 0 12 18" fill="none" stroke="#fff" stroke-width="2"><rect x="1" y="1" width="10" height="16" rx="2"/></svg></i>(02) 9000 4321
  </span>
</div>

<header class="site-header">
  <span class="brand-mark"></span>
  <div class="brand-name">WHOLE HEART LIVING</div>
  <div class="brand-sub">PSYCHOLOGY &amp; COUNSELLING RELATIONSHIP CENTRE</div>
  <nav class="nav">
    <svg width="16" height="15" viewBox="0 0 16 15" fill="var(--green)"><path d="M8 0l8 7h-2v8h-4v-5H6v5H2V7H0z"/></svg>
    <span>How We Can Help</span><span>Relationship Counselling</span><span>Parenting</span><span>Courses</span><span>Our Team</span><span>Services</span><span>Contact</span>
  </nav>
</header>

<section class="hero">
  <div class="photo" role="img" aria-label="Photo of a counsellor sitting with a young boy"></div>
  <h1>Whole Heart Living<br>Psychology &amp; Counselling<br>Relationship Centre</h1>
  <div class="tag">We Will Respond to You Within 24 hours</div>
  <div class="btn" style="left:77px;top:350px;width:266px;height:51px">Book an Appointment</div>
  <div class="arrow" style="left:15px"><svg width="12" height="20" viewBox="0 0 12 20" fill="none" stroke="#8fb0d4" stroke-width="1.5"><path d="M10 2L2 10l8 8"/></svg></div>
  <div class="arrow" style="left:1144px"><svg width="12" height="20" viewBox="0 0 12 20" fill="none" stroke="#8fb0d4" stroke-width="1.5"><path d="M2 2l8 8-8 8"/></svg></div>
</section>

<section class="who">
  <div class="frame"></div>
  <div class="photo" role="img" aria-label="Photo of a counsellor taking notes with a client"></div>
  <h2 class="h2">Who We <span>Help</span></h2>
  <p>Whole Heart Living Psychology and Counselling Relationship Centre is a team of highly trained professionals provide the ultimate in wellbeing treatment for children, teenagers, adults, parents and couples. We have a strong reputation for providing a warm and personalised service using research based approaches.</p>
  <div class="btn" style="left:637px;top:346px;width:166px;height:51px">Learn More</div>
</section>

<section class="expect">
  <h2 class="h2">What to <span>Expect</span></h2>
  <p class="lead">Sometimes people don't know what to expect from the counselling processes. You may wonder if your issues are too complicated, or not serious enough, or worry that the things you'll discuss will be so distressing that you'll carry the pain around with you, long after leaving the session.</p>

  <div class="mini" style="left:84px;top:282px;background:#a7b6c4" role="img" aria-label="Photo of a couple in a session"></div>
  <div class="group left" style="left:217px;top:303px"><h3>Couples</h3><p>Treatment for<br>couples over 18<br>years old.</p></div>

  <div class="mini" style="left:84px;top:462px;background:#6e8fb3" role="img" aria-label="Photo of a family at home"></div>
  <div class="group left" style="left:217px;top:481px"><h3>Parenting</h3><p>Treatment for<br>couples over 18<br>years old.</p></div>

  <div class="group right" style="left:726px;top:303px"><h3>Children &amp;<br>Teenagers</h3><p>Treatment for<br>couples over 18<br>years old.</p></div>
  <div class="mini" style="left:1014px;top:282px;background:#d9c4bd" role="img" aria-label="Photo of a young girl"></div>

  <div class="group right" style="left:726px;top:481px"><h3>Adults</h3><p>Treatment for<br>couples over 18<br>years old.</p></div>
  <div class="mini" style="left:1014px;top:462px;background:#b8c4b5" role="img" aria-label="Photo of two adults talking"></div>

  <div class="feature-photo" role="img" aria-label="Collage of photos of a family, a child and a couple"></div>
</section>

<section class="courses">
  <h2 class="h2">Our Courses</h2>
  <div class="sub">Below is a List of Some of the Courses We Conduct</div>
  <div class="tabs">
    <span class="tab active">Parenting</span>
    <span class="tab">Couple Communication</span>
    <span class="tab">Anger management</span>
    <span class="tab">Anxiety</span>
    <span class="tab">Assertiveness Training</span>
    <span class="tab">Secure Bonds</span>
  </div>
  <div class="course-card">
    <div class="photo" role="img" aria-label="Photo of a girl covering her ears in a kitchen"></div>
    <h3>PARENTING</h3>
    <p>Whole Heart Living Psychology and Counselling Relationship Centre offers experienced Parent Attachment Experts to help you with any parenting issues you are facing</p>
    <div class="btn" style="left:566px;top:253px;width:166px;height:51px">Learn More</div>
  </div>
</section>

<section class="touch">
  <h2 class="h2">Keep in <span>Touch</span></h2>
  <p class="lead">To make a confidential enquiry or to request an initial chat over the phone or to book an appointment</p>
  <div class="rule"></div>
  <div class="contact" style="left:151px">
    <div class="ring"><div class="dot"><svg width="22" height="22" viewBox="0 0 24 24" fill="#fff"><path d="M6.6 10.8a15.1 15.1 0 0 0 6.6 6.6l2.2-2.2c.3-.3.7-.4 1-.2 1.1.4 2.3.6 3.6.6.6 0 1 .4 1 1V20c0 .6-.4 1-1 1C10.6 21 3 13.4 3 4c0-.6.4-1 1-1h3.5c.6 0 1 .4 1 1 0 1.3.2 2.5.6 3.6.1.3 0 .7-.2 1z"/></svg></div></div>
    <h4>Call Us</h4><span>0400 111 333</span>
  </div>
  <div class="contact" style="left:450px">
    <div class="ring"><div class="dot"><svg width="16" height="22" viewBox="0 0 12 18" fill="none" stroke="#fff" stroke-width="1.8"><rect x="1" y="1" width="10" height="16" rx="2"/><path d="M5 14h2"/></svg></div></div>
    <h4>Email Us</h4><span style="letter-spacing:.2px">hello@wholeheartliving.example</span>
  </div>
  <div class="contact" style="left:740px">
    <div class="ring"><div class="dot"><svg width="22" height="22" viewBox="0 0 24 24" fill="none" stroke="#fff" stroke-width="2"><path d="M20 13v7H4V4h7"/><path d="M17 3l4 4-9 9H8v-4z"/></svg></div></div>
    <h4>Text Us</h4><span>(02) 9000 4321</span>
  </div>
  <div class="respond">We will respond to you within <b>24</b> hours</div>
  <div class="forward">We look forward to working with you</div>
  <div class="photo" role="img" aria-label="Photo of five smiling young people using phones and a laptop"></div>
</section>

<section class="booking">
  <h3>Online Hassle Free Appointment Booking</h3>
  <p>Marriage Counselling / Parenting Issues / Relationship Issues</p>
  <div class="outline">Book an Appointment</div>
</section>

<footer class="site-footer">
  <div class="foot-brand">
    <div class="mark"></div>
    <div class="name">WHOLE HEART LIVING</div>
    <div class="sub">PSYCHOLOGY &amp; COUNSELLING RELATIONSHIP CENTRE</div>
  </div>
  <span class="social" style="left:125px" aria-label="Social link"></span>
  <span class="social" style="left:175px" aria-label="Social link"></span>
  <span class="social" style="left:224px" aria-label="Social link"></span>

  <div class="col" style="left:338px">
    <h5>Site<span>map</span></h5>
    <ul><li>How We Can Help</li><li>Relationship Counselling</li><li>Parenting</li><li>Courses</li><li>Our Team</li><li>Contact</li></ul>
  </div>
  <div class="col" style="left:598px">
    <h5>Quick <span>Links</span></h5>
    <ul><li>Terms &amp; Condition</li><li>Privacy Policy</li><li>Legal Disclaimer</li><li>Sitemap</li></ul>
  </div>
  <div class="col" style="left:838px">
    <h5>Newsletter <span>Signup !</span></h5>
    <p class="note">Would you like to receive our Exclusive update for signup !</p>
    <div class="field">Enter Email *</div>
    <div class="subscribe">Subscribe</div>
  </div>
  <div class="copy">©Whole Heart Living - 2019 All Rights Reserved.</div>
</footer>

</body>
</html>
```